Company Real Estate Site Needs A Face Lift

I need a new website for the recent company I formed: Voska Real Estate.
You can use my agent website WWW.PALMIROQ.COM to see the style/brand I already have. I will have areas for Searching for homes on IDX, etc.
I really like this site:
http://www.cranfeltmanorhomes.com/
I have attached my logo as well

Industry/Entity Type

Real Estate

Colors
0255a3
ffffff
cee9f5

```html
<!DOCTYPE html>
<html lang="en">
<head>
<meta charset="utf-8">
<title>Voska Real Estate</title>
<link href="https://fonts.googleapis.com/css2?family=Open+Sans:wght@300;400;600&display=swap" rel="stylesheet">
<style>
:root{
  --brand-blue:#0255a3;
  --brand-blue-dark:#073a78;
  --footer-deep:#0a2f63;
  --pale-blue:#cee9f5;
  --pale-blue-light:#e3f3fa;
  --white:#ffffff;
  --text:#555a60;
  --heading:#2d3035;
  --gray-panel:#8a8a8a;
}
*{margin:0;padding:0;box-sizing:border-box}
html,body{width:1037px;height:1200px;overflow:hidden;background:var(--white)}
body{font-family:"Open Sans",sans-serif;color:var(--text);position:relative}
.hero{position:absolute;left:0;top:0;width:1037px;height:550px;overflow:hidden}
.hero-photo{position:absolute;inset:0;
  background:linear-gradient(90deg,#b9a68c 0%,#d9cdb9 30%,#e9e2d6 50%,#9fc9c8 75%,#5fb5c0 88%,#d8d0c2 100%)}
.hero-shapes{position:absolute;left:0;top:0}
.site-nav{position:absolute;right:0;top:0;width:706px;height:83px;color:var(--white)}
.phone{position:absolute;right:96px;top:9px;font-size:20px;display:flex;align-items:center;gap:5px}
.menu{position:absolute;right:96px;top:45px;display:flex;gap:30px;list-style:none;font-size:14px}
.brand{position:absolute;left:70px;top:85px;font-size:28px;font-weight:600;color:var(--white);letter-spacing:1px}
.caption{position:absolute;left:0;top:255px;width:543px;height:152px;background:rgba(255,255,255,.86);
  clip-path:polygon(0 0,100% 0,84% 100%,0 100%)}
.caption .kicker{position:absolute;left:159px;top:25px;font-size:19px;color:#222;font-weight:400}
.caption .title{position:absolute;left:159px;top:50px;font-size:28px;color:#111;font-weight:400}
.caption .lede{position:absolute;left:159px;top:88px;font-size:11px;line-height:19px;color:#777;font-weight:300;width:300px}
.dots{position:absolute;left:479px;top:525px;display:flex;gap:5px}
.dots span{width:13px;height:13px;border-radius:50%;background:#8e8e8e}
.about{position:absolute;left:88px;top:596px;width:285px}
h2{font-size:20px;font-weight:400;color:var(--heading)}
.about p{font-size:11px;line-height:18.7px;margin-top:9px}
.about h2+p{margin-top:12px}
.search{position:absolute;left:394px;top:591px;width:261px;height:293px;
  background:linear-gradient(180deg,var(--pale-blue-light),var(--pale-blue));padding:21px 24px}
.search h2,.projects h2{color:var(--brand-blue)}
.search .sub{font-size:11.5px;color:var(--brand-blue);margin-top:1px;margin-bottom:12px}
.field{height:26px;border:1px solid #a9cde0;background:#f4fafd;font-size:10px;color:#2f5a80;
  padding:0 8px;display:flex;align-items:center;justify-content:space-between;margin-bottom:7px}
.field .caret{width:0;height:0;border:4px solid transparent;border-top:5px solid var(--brand-blue);margin-top:4px}
.field-row{display:flex;gap:10px}.field-row .field{flex:1}
.btn{display:inline-block;margin-top:3px;background:var(--brand-blue-dark);color:var(--white);font-size:13px;font-weight:600;
  padding:8px 20px}
.projects{position:absolute;left:687px;top:596px;width:280px}
.project{display:flex;gap:10px;margin-top:12px;height:75px}
.project:first-of-type{margin-top:13px}
.thumb{width:84px;height:65px;flex:none}
.project h3{font-size:13px;font-weight:400;color:#444;margin-top:-2px}
.project p{font-size:10px;line-height:17px;color:#777;margin-top:2px}
.site-footer{position:absolute;left:0;top:925px;width:1037px;height:227px;
  background:linear-gradient(180deg,#1f62a8,#0c4586)}
.col{position:absolute;top:29px;color:var(--white)}
.col h4{font-size:19px;font-weight:400;margin-bottom:8px}
.col li{list-style:none;font-size:11px;font-weight:600;height:24px;line-height:15px}
.col .big{font-size:15px}
.social{display:flex;gap:6px;margin-top:2px}
.social span{width:20px;height:20px;border-radius:50%;background:var(--white)}
.legal{position:absolute;left:0;top:1152px;width:1037px;height:48px;background:var(--footer-deep);
  color:#8ca4c6;font-size:11px;padding:16px 0 0 86px}
</style>
</head>
<body>
<header class="hero">
  <div class="hero-photo" role="img" aria-label="Bright bedroom opening onto a terrace with an infinity pool and sea view"></div>
  <svg class="hero-shapes" width="1037" height="550" viewBox="0 0 1037 550">
    <polygon points="0,0 398,0 0,407" fill="var(--gray-panel)"/>
    <polygon points="398,0 412,0 0,421 0,407" fill="var(--white)"/>
    <polygon points="412,0 1037,0 1037,83 331,83" fill="var(--brand-blue)"/>
  </svg>
  <div class="brand">Voska Real Estate</div>
  <nav class="site-nav">
    <div class="phone">
      <svg width="14" height="16" viewBox="0 0 24 24"><path fill="#cfe3f5" d="M6.6 10.8c1.4 2.8 3.8 5.1 6.6 6.6l2.2-2.2c.3-.3.7-.4 1-.2 1.1.4 2.3.6 3.6.6.6 0 1 .4 1 1V20c0 .6-.4 1-1 1C10.6 21 3 13.4 3 4c0-.6.4-1 1-1h3.5c.6 0 1 .4 1 1 0 1.3.2 2.5.6 3.6.1.3 0 .7-.2 1z"/></svg>
      555.014.2288
    </div>
    <ul class="menu"><li>HOME</li><li>ABOUT US</li><li>BUY</li><li>SELL</li><li>TESTIMONIALS</li><li>BLOG</li><li>CONTACT</li></ul>
  </nav>
  <div class="caption">
    <div class="kicker">CUM SOCIIS NATOQUE PENATIBU</div>
    <div class="title">ETIAM EU URNA SED</div>
    <div class="lede">Vivamus porttitor g purus nisi eleifend libero a tempus libero lectus feugiat felis Morbi diam mauris viverr</div>
  </div>
  <div class="dots"><span></span><span></span><span></span><span></span></div>
</header>

<section class="about">
  <h2>ABOUT OUR COMPANY</h2>
  <p>Palmiroq.Com is designed to make your online research of the Harlow Creek Real Estate /Ashbury Falls Real Estate Market/Milbrook Point Real Estate Market as “simple” as possible.</p>
  <p>My theory is that some people wish to remain anony-mous, at first, when thinking of buying a home or selling Harlow Creek Real Estate &amp; wish not to be bothered by someone calling them all the time. As a Realtor in Harlow Creek, I respect ones privacy and will let the knowledge and usefulness of my site speak for itself. When you are ready get moving, then I’m ready to help. Until then, kick back and “simply”</p>
</section>

<section class="search">
  <h2>SEARCH PROPERTY</h2>
  <div class="sub">Mauris vel lacus vitae felis vestibulum</div>
  <div class="field">Property Type<span class="caret"></span></div>
  <div class="field-row">
    <div class="field">Bedroom<span class="caret"></span></div>
    <div class="field">Bathroom<span class="caret"></span></div>
  </div>
  <div class="field">Location/Place</div>
  <div class="field">By Address</div>
  <div class="field">Near Railway Station, Airport etc</div>
  <span class="btn">SEARCH NOW</span>
</section>

<section class="projects">
  <h2>LATEST PROJECTS</h2>
  <div class="project">
    <div class="thumb" role="img" aria-label="City buildings under a pale sky" style="background:linear-gradient(180deg,#dfe6ee,#a0523e)"></div>
    <div><h3>Vivamus porttitor purus</h3><p>nisi eleifend libero a tempus libero lectus feugiat felis Morbi diam mauris viverra</p></div>
  </div>
  <div class="project">
    <div class="thumb" role="img" aria-label="Lit modern building at dusk" style="background:linear-gradient(135deg,#2c4a9a,#d8a64a)"></div>
    <div><h3>Vivamus porttitor purus</h3><p>nisi eleifend libero a tempus libero lectus feugiat felis Morbi diam mauris viverra</p></div>
  </div>
  <div class="project">
    <div class="thumb" role="img" aria-label="Suspension bridge at sunset" style="background:linear-gradient(180deg,#e08a3a,#6a2a1a)"></div>
    <div><h3>Vivamus porttitor purus</h3><p>nisi eleifend libero a tempus libero lectus feugiat felis Morbi diam mauris viverra</p></div>
  </div>
</section>

<footer class="site-footer">
  <div class="col" style="left:88px"><h4>Company</h4><ul><li>ADVANCED SEARCH</li><li>MAP SEARCH</li><li>ADDRESS SEARCH</li><li>OUR FEATURED LISTINGS</li><li>LISTING MANAGER LOGIN</li></ul></div>
  <div class="col" style="left:292px"><h4>Sublinks</h4><ul><li>EMAIL UPDATES SIGNUP</li><li>LISTING ID SEARCH</li><li>OPEN HOUSES</li><li>SOLD/PENDING LISTINGS</li><li>HOME VALUATION REQUEST</li></ul></div>
  <div class="col" style="left:508px"><h4>Support</h4><ul><li>CUSTOMER SUPPORT</li><li>FAQ</li><li>RECENT BLOG POST</li><li>TESTIMONIALS</li><li>CONTACT US</li></ul></div>
  <div class="col" style="left:689px"><h4>Contact Info</h4><ul><li>72 LARKMOOR RIDGE ROAD SUITE 310</li><li>FENWICK HOLLOW, WN 20417</li><li class="big">555-013-4471</li><li class="big">555-013-4482</li></ul>
    <div class="social"><span></span><span></span><span></span></div></div>
</footer>
<div class="legal">© 2014 Company Name&nbsp; All right reserved&nbsp; Term of Use</div>
</body>
</html>
```